Business Brochure for Mobile Fleet Mechanic Company

Make a brochure for an mobile mechanic company that is a Bi-fold 8.5"Wx11"H. A Bi-fold would have the outside and inside design so it is a total of 4 pages at 8.5"x11". The print is 2-sides 17"Wx11"H that folds down to 8.5"Wx11"H.
Should have photo of mechanic working. Blue in logo is Pantone 284C. Will provide text to be added to approved design.

Contact Information for Business Card

2-sided card using the same design elements and colors as the brochure.

```html
<!DOCTYPE html>
<html lang="en">
<head>
<meta charset="utf-8">
<title>RigMend Bi-fold Brochure</title>
<link href="https://fonts.googleapis.com/css2?family=Montserrat:wght@400;500;600;700;800&display=swap" rel="stylesheet">
<style>
  :root{
    --backdrop:#4b4b4d;
    --paper:#ffffff;
    --brand-blue:#5f8fcb;
    --blue-light:#7fa8da;
    --charcoal:#3b3d43;
    --ink:#2f3034;
    --rule:#c9d6e8;
  }
  *{box-sizing:border-box;margin:0;padding:0}
  html,body{width:911px;height:1200px;overflow:hidden}
  body{background:var(--backdrop);font-family:"Montserrat",sans-serif;color:var(--ink);position:relative}
  .spread{position:absolute;left:20px;width:871px;height:564px;background:var(--paper);overflow:hidden;box-shadow:0 6px 18px rgba(0,0,0,.35)}
  .spread--outside{top:24px}
  .spread--inside{top:612px}
  .fold{position:absolute;left:435px;top:0;width:1px;height:100%;background:rgba(0,0,0,.08)}
  .abs{position:absolute}

  /* outside */
  .photo-workshop{left:0;top:0;width:436px;height:400px;background:linear-gradient(120deg,#1e4f93 0%,#2a6fc0 35%,#cfe3ee 55%,#9fc3dc 75%,#27508c 100%)}
  .photo-mechanic{left:436px;top:0;width:435px;height:300px;background:linear-gradient(150deg,#1d4f97 0%,#3a78c4 30%,#d7e6ee 48%,#8c95a1 70%,#4d525c 100%)}
  .divider{left:0;top:0;width:871px;height:564px}
  .wordmark{font-weight:700;color:var(--brand-blue);display:flex;align-items:center;gap:6px;letter-spacing:.3px}
  .wordmark .mark{width:10px;height:10px;background:currentColor}
  .wordmark--back{left:40px;top:470px;font-size:20px}
  .wordmark--front{right:40px;top:40px;font-size:24px;color:#fff}
  .contacts{font-size:8.5px;color:var(--ink);line-height:1.55}
  .contacts--a{left:175px;top:460px}
  .contacts--b{left:300px;top:450px}
  .contact-row{display:flex;align-items:center;gap:5px}
  .contact-row svg{width:9px;height:9px;flex:none}
  .headline{right:36px;top:372px;text-align:right;font-weight:800;line-height:1.02}
  .headline .line-blue{color:var(--blue-light);font-size:32px;display:block}
  .headline .line-dark{color:var(--ink);font-size:34px;display:block}
  .headline .web{font-size:9.5px;letter-spacing:2.5px;font-weight:500;color:var(--ink);display:block;margin-top:8px}

  /* inside left */
  .photo-engine{left:24px;top:20px;width:150px;height:100px;background:radial-gradient(ellipse at center,#8a8e95 0%,#5d6168 55%,rgba(255,255,255,0) 75%)}
  .section-title{font-size:11px;font-weight:600;color:var(--brand-blue);display:flex;align-items:center;gap:6px}
  .section-title::before{content:"";width:6px;height:6px;background:var(--charcoal);flex:none}
  .body-copy{font-size:7.4px;line-height:1.45;color:var(--ink)}
  .intro{left:190px;top:22px;width:225px}
  .intro .body-copy{margin-top:5px}
  .band-dark{left:0;top:150px;width:436px;height:118px;background:var(--charcoal)}
  .band-dark .section-title{color:var(--blue-light);position:absolute;left:24px;top:12px}
  .band-dark .section-title::before{background:#fff}
  .bullets{position:absolute;top:32px;width:190px;list-style:none;font-size:7.4px;line-height:1.35;color:#e7e9ee}
  .bullets li{margin-bottom:5px;padding-left:7px;position:relative}
  .bullets li::before{content:"•";position:absolute;left:0}
  .bullets--1{left:24px}
  .bullets--2{left:228px}
  .passage{left:24px;top:282px;width:390px}
  .passage .body-copy{margin-top:6px}
  .quote-band{left:0;top:398px;width:436px;height:62px;background:var(--brand-blue)}
  .quote-text{position:absolute;left:40px;top:14px;width:220px;font-size:9px;font-weight:800;color:#fff;text-transform:uppercase;line-height:1.3;letter-spacing:.4px}
  .photo-tires{left:282px;top:380px;width:100px;height:100px;background:radial-gradient(ellipse at center,#3a3b3f 0%,#1f2023 60%,rgba(0,0,0,0) 72%)}
  .base{left:0;top:0;width:871px;height:564px}

  /* inside right */
  .why{left:470px;top:30px;width:210px}
  .why .section-title{font-weight:500}
  .why .lead{font-size:8.5px;font-weight:700;margin-top:8px;line-height:1.35}
  .why .body-copy{margin-top:5px}
  .ticks{position:absolute;left:470px;top:140px;width:210px;list-style:none}
  .ticks li{display:flex;align-items:center;gap:14px;height:52px;border-bottom:1px solid var(--rule);font-size:8.4px;font-weight:700;line-height:1.3}
  .ticks svg{width:18px;height:18px;flex:none}
  .service{left:694px;top:40px;width:177px;height:440px;background:var(--brand-blue);color:#fff;padding:18px 16px}
  .service h3{font-size:11px;font-weight:500}
  .service .body-copy{color:#eef3fa;margin-top:5px}
  .service-list{list-style:none;margin-top:16px}
  .service-list li{display:flex;align-items:center;gap:14px;height:55px;border-bottom:1px solid rgba(255,255,255,.45);font-size:8px;font-weight:700;line-height:1.3}
  .service-list svg{width:22px;height:18px;flex:none}
  .service .foot{position:absolute;left:16px;bottom:14px;width:150px;font-size:7.4px;line-height:1.4;color:#eef3fa}
</style>
</head>
<body>

<section class="spread spread--outside" aria-label="Outside spread: back and front cover">
  <div class="abs photo-workshop" role="img" aria-label="Photo of a blue-walled workshop with tool wall and glass-block window"></div>
  <div class="abs photo-mechanic" role="img" aria-label="Photo of a mechanic working under the open hood of a car"></div>

  <svg class="abs divider" viewBox="0 0 871 564" aria-hidden="true">
    <path d="M0 400 L398 400 L422 300 L448 415 L472 300 L871 300 L871 564 L0 564 Z" fill="#fff"/>
    <path d="M0 400 L398 400 L422 300 L448 415 L472 300 L871 300" fill="none" stroke="#55585f" stroke-width="4" stroke-linejoin="miter"/>
  </svg>

  <div class="abs wordmark wordmark--back"><span class="mark"></span>RigMend</div>
  <div class="abs contacts contacts--a">
    <div class="contact-row"><svg viewBox="0 0 10 10"><path d="M2 1l2 2-1 1.5a6 6 0 0 0 2.5 2.5L7 6l2 2-1.5 1.5C4 9 1 6 .5 2.5Z" fill="#5f8fcb"/></svg><b>555-010-2040</b></div>
    <div class="contact-row"><svg viewBox="0 0 10 10"></svg><b>555-010-3050</b></div>
    <div class="contact-row"><svg viewBox="0 0 10 10"><rect x="1" y="2.5" width="8" height="5.5" fill="#5f8fcb"/><path d="M1 2.5l4 3 4-3" stroke="#fff" fill="none" stroke-width=".8"/></svg>info@rigmend.com</div>
  </div>
  <div class="abs contacts contacts--b">
    <div class="contact-row"><svg viewBox="0 0 10 10"><circle cx="5" cy="5" r="4" fill="none" stroke="#5f8fcb" stroke-width="1.2"/><path d="M1 5h8M5 1v8" stroke="#5f8fcb" stroke-width=".8"/></svg>www.rigmend.com</div>
    <div class="contact-row"><svg viewBox="0 0 10 10"><path d="M5 9.5S1.5 6 1.5 4a3.5 3.5 0 0 1 7 0c0 2-3.5 5.5-3.5 5.5Z" fill="#5f8fcb"/><circle cx="5" cy="4" r="1.2" fill="#fff"/></svg>18 Harbor Lane,</div>
    <div class="contact-row"><svg viewBox="0 0 10 10"></svg>Millbrook, TN 37000</div>
  </div>

  <div class="abs wordmark wordmark--front"><span class="mark"></span>RigMend</div>
  <div class="abs headline">
    <span class="line-blue">Great Deals</span>
    <span class="line-dark">Great Service</span>
    <span class="web">www.rigmend.com</span>
  </div>
  <div class="fold"></div>
</section>

<section class="spread spread--inside" aria-label="Inside spread">
  <svg class="abs base" viewBox="0 0 871 564" aria-hidden="true">
    <path d="M0 482 L392 482 L412 440 L436 505 L458 450 L871 545 L871 564 L0 564 Z" fill="#3b3d43"/>
    <path d="M0 476 L390 476 L411 432 L436 498" fill="none" stroke="#5f8fcb" stroke-width="3"/>
  </svg>

  <div class="abs photo-engine" role="img" aria-label="Photo of a car engine block"></div>
  <div class="abs intro">
    <h2 class="section-title">Lorem Ipsum</h2>
    <p class="body-copy">Lorem Ipsum is simply dummy text of the printing and typesetting industry. Lorem Ipsum has been the industry's standard dummy text ever since the 1500s, when an unknown printer took a galley of type and scrambled it to make a type specimen book. It has survived not only five centuries, but also the leap into electronic typesetting, remaining essentially unchanged.</p>
  </div>

  <div class="abs band-dark">
    <h2 class="section-title">Lorem Ipsum</h2>
    <ul class="bullets bullets--1">
      <li>Sed ut perspiciatis unde omnis iste natus sit voluptatem.</li>
      <li>Sed ut perspiciatis unde omnis iste natus sit voluptatem.</li>
      <li>Sed ut perspiciatis unde omnis iste natus sit voluptatem.</li>
    </ul>
    <ul class="bullets bullets--2">
      <li>Sed ut perspiciatis unde omnis iste natus sit voluptatem.</li>
      <li>Sed ut perspiciatis unde omnis iste natus sit voluptatem.</li>
      <li>Sed ut perspiciatis unde omnis iste natus sit voluptatem.</li>
    </ul>
  </div>

  <div class="abs passage">
    <h2 class="section-title">The standard Lorem Ipsum passage</h2>
    <p class="body-copy">At vero eos et accusamus et iusto odio dignissimos ducimus qui blanditiis praesentium voluptatum deleniti atque corrupti quos dolores et quas molestias excepturi sint occaecati cupiditate non provident, similique sunt in culpa qui officia deserunt mollitia animi, id est laborum et dolorum fuga.</p>
    <p class="body-copy">On the other hand, we denounce with righteous indignation and dislike men who are so beguiled, which is the same as saying through shrinking from toil and pain. These cases are perfectly simple and easy to distinguish.</p>
  </div>

  <div class="abs quote-band">
    <p class="quote-text">“On the other hand, we denounce the pleasure of the moment, so blinded by desire”</p>
  </div>
  <div class="abs photo-tires" role="img" aria-label="Photo of a stack of car tyres"></div>

  <div class="abs why">
    <h2 class="section-title">Why we?</h2>
    <p class="lead">There are many variations of passages of Lorem Ipsum.</p>
    <p class="body-copy">There are many variations of passages of Lorem Ipsum available, but the majority have suffered alteration in some form, by injected humour.</p>
  </div>
  <ul class="ticks">
    <li><svg viewBox="0 0 18 18"><circle cx="9" cy="9" r="7.5" fill="none" stroke="#5f8fcb" stroke-width="1.4"/><path d="M5.5 9.2l2.4 2.3 4.6-5" fill="none" stroke="#5f8fcb" stroke-width="1.6"/></svg>There are many tions of passages of Lorem Ipsum.</li>
    <li><svg viewBox="0 0 18 18"><circle cx="9" cy="9" r="7.5" fill="none" stroke="#5f8fcb" stroke-width="1.4"/><path d="M5.5 9.2l2.4 2.3 4.6-5" fill="none" stroke="#5f8fcb" stroke-width="1.6"/></svg>There are many tions of passages of Lorem Ipsum.</li>
    <li><svg viewBox="0 0 18 18"><circle cx="9" cy="9" r="7.5" fill="none" stroke="#5f8fcb" stroke-width="1.4"/><path d="M5.5 9.2l2.4 2.3 4.6-5" fill="none" stroke="#5f8fcb" stroke-width="1.6"/></svg>There are many tions of passages of Lorem Ipsum.</li>
    <li><svg viewBox="0 0 18 18"><circle cx="9" cy="9" r="7.5" fill="none" stroke="#5f8fcb" stroke-width="1.4"/><path d="M5.5 9.2l2.4 2.3 4.6-5" fill="none" stroke="#5f8fcb" stroke-width="1.6"/></svg>There are many tions of passages of Lorem Ipsum.</li>
    <li><svg viewBox="0 0 18 18"><circle cx="9" cy="9" r="7.5" fill="none" stroke="#5f8fcb" stroke-width="1.4"/><path d="M5.5 9.2l2.4 2.3 4.6-5" fill="none" stroke="#5f8fcb" stroke-width="1.6"/></svg>There are many tions of passages of Lorem Ipsum.</li>
  </ul>

  <aside class="abs service">
    <h3>Service:</h3>
    <p class="body-copy">There are many variations of sages of Lorem Ipsum available, but the majority have suffered alteration in some form, by injected humour.</p>
    <ul class="service-list">
      <li><svg viewBox="0 0 22 18"><path d="M3 11l2-5h12l2 5v4H3Z" fill="#fff"/><circle cx="7" cy="15" r="1.8" fill="#5f8fcb"/><circle cx="15" cy="15" r="1.8" fill="#5f8fcb"/></svg>There are manytions of Lorem Ipsum.</li>
      <li><svg viewBox="0 0 22 18"><path d="M3 11l2-5h12l2 5v4H3Z" fill="#fff"/><circle cx="7" cy="15" r="1.8" fill="#5f8fcb"/><circle cx="15" cy="15" r="1.8" fill="#5f8fcb"/></svg>There are manytions of Lorem Ipsum.</li>
      <li><svg viewBox="0 0 22 18"><path d="M3 11l2-5h12l2 5v4H3Z" fill="#fff"/><circle cx="7" cy="15" r="1.8" fill="#5f8fcb"/><circle cx="15" cy="15" r="1.8" fill="#5f8fcb"/></svg>There are manytions of Lorem Ipsum.</li>
      <li><svg viewBox="0 0 22 18"><path d="M3 11l2-5h12l2 5v4H3Z" fill="#fff"/><circle cx="7" cy="15" r="1.8" fill="#5f8fcb"/><circle cx="15" cy="15" r="1.8" fill="#5f8fcb"/></svg>There are manytions of Lorem Ipsum.</li>
      <li><svg viewBox="0 0 22 18"><path d="M3 11l2-5h12l2 5v4H3Z" fill="#fff"/><circle cx="7" cy="15" r="1.8" fill="#5f8fcb"/><circle cx="15" cy="15" r="1.8" fill="#5f8fcb"/></svg>There are manytions of Lorem Ipsum.</li>
    </ul>
    <p class="foot">Lorem Ipsum is therefore always free from repetition, injected humour, or non-characteristic words etc.</p>
  </aside>
  <div class="fold"></div>
</section>

</body>
</html>
```